Terravane Business Card Design

We need a modern, clean, business card design for our hardscape solution company. I have outlined our specialist areas in the card information section. We meet and greet and wish to build relationships with large-scale builders and project managers of large-scale building companies. Hence the reason for the business card.We want them to understand we are their 'solution' and we will make their working life easier and less stressful. We also are the highest quality construction with an exceptional eye for detail taking a lot of pressure off the project managers. I have done a few mock-ups myself but would like to see what else can be created. We are open to black or white (or grey) background.

Industry/Entity Type

Construction

Contact Information for Business Card

Mark Quinlow - Director
0417 583 902
mark@terravanegroup.com

www.terravanegroup.com.au

"Hardscape Construction Solutions for Large-Scale Builders" (front)

Logo already designed and to be added.

REAR:

Your One-Stop Hardscape Solution For:

Retirement Village & Community Development Construction

- Synthetic Sports Fields - Bowling Greens
- Tennis Courts - Concreting
- Paving - Landscape

www.terravanegroup.com

```html
<!DOCTYPE html>
<html lang="en">
<head>
<meta charset="utf-8">
<title>Terravane Business Card</title>
<link rel="stylesheet" href="https://fonts.googleapis.com/css2?family=Lato:ital,wght@0,400;0,700;0,900;1,700&display=swap">
<style>
  :root {
    --canvas: #e4e2de;
    --card: #111213;
    --card-stripe: #1a1b1d;
    --lime: #c4d92a;
    --blue: #1e8fd6;
    --white: #f2f2f2;
  }
  * { box-sizing: border-box; margin: 0; padding: 0; }
  html, body { width: 1200px; height: 1000px; overflow: hidden; }
  body {
    background: var(--canvas);
    font-family: "Lato", sans-serif;
    position: relative;
  }
  .card {
    position: absolute;
    left: 215px;
    width: 770px;
    height: 440px;
    background:
      repeating-linear-gradient(90deg, var(--card) 0 3px, var(--card-stripe) 3px 5px);
    overflow: hidden;
    box-shadow: 0 10px 28px rgba(0,0,0,.28);
  }
  .card--front { top: 40px; }
  .card--back { top: 520px; }
  .swoosh { position: absolute; inset: 0; width: 100%; height: 100%; }

  /* front */
  .brand {
    position: absolute; right: 50px; top: 42px;
    font-weight: 900; font-size: 70px; letter-spacing: -1px;
    color: var(--blue); line-height: 1;
  }
  .tagline {
    position: absolute; right: 50px; top: 138px;
    font-style: italic; font-weight: 700; font-size: 16px;
    color: var(--white);
  }
  .person { position: absolute; left: 55px; top: 72px; }
  .person__name {
    font-weight: 700; font-size: 25px; color: var(--lime);
    text-transform: uppercase; letter-spacing: .5px;
  }
  .person__role { font-size: 18px; color: var(--blue); }
  .contact {
    position: absolute; left: 395px; top: 200px;
    list-style: none; font-size: 20px; line-height: 1.5;
    color: var(--white);
  }
  .contact__label { color: var(--blue); font-weight: 700; }

  /* back */
  .services { position: absolute; left: 60px; top: 50px; right: 50px; }
  .services__heading { font-weight: 700; font-size: 27px; color: var(--blue); }
  .services__sector { font-weight: 700; font-size: 20px; color: var(--white); margin-top: 12px; }
  .services__list {
    list-style: none; margin-top: 30px;
    display: grid; grid-template-columns: 330px 1fr; row-gap: 18px;
    grid-auto-flow: column; grid-template-rows: repeat(3, auto);
  }
  .services__item {
    font-weight: 700; font-size: 22px; color: var(--lime);
    display: flex; align-items: center; gap: 14px;
  }
  .services__bullet { width: 30px; height: 14px; flex: none; }
</style>
</head>
<body>

<section class="card card--front" aria-label="Business card front">
  <svg class="swoosh" viewBox="0 0 770 440" preserveAspectRatio="none" aria-hidden="true">
    <defs>
      <linearGradient id="limeFront" x1="0" y1="0" x2="1" y2="1">
        <stop offset="0" stop-color="#eef47a"/>
        <stop offset="1" stop-color="#b8d11e"/>
      </linearGradient>
    </defs>
    <path d="M0 250 C150 200 260 230 330 320 C390 390 520 420 770 408 L770 432 C520 442 380 425 305 355 C245 290 140 262 0 288 Z" fill="url(#limeFront)"/>
  </svg>
  <div class="brand">Terravane</div>
  <p class="tagline">"Hardscape Construction Solutions for Large-Scale Builders"</p>
  <div class="person">
    <p class="person__name">Mark Quinlow</p>
    <p class="person__role">Director</p>
  </div>
  <ul class="contact">
    <li><span class="contact__label">Phone:</span> 0417 583 902</li>
    <li><span class="contact__label">Email:</span> mark@terravanegroup.com</li>
    <li><span class="contact__label">Website:</span> www.terravanegroup.com.au</li>
  </ul>
</section>

<section class="card card--back" aria-label="Business card back">
  <svg class="swoosh" viewBox="0 0 770 440" preserveAspectRatio="none" aria-hidden="true">
    <defs>
      <linearGradient id="limeBack" x1="0" y1="1" x2="1" y2="0">
        <stop offset="0" stop-color="#b8d11e"/>
        <stop offset="1" stop-color="#eef47a"/>
      </linearGradient>
    </defs>
    <path d="M0 440 C150 380 300 350 450 355 C600 360 700 330 770 290 L770 320 C690 380 600 400 470 400 C330 400 200 420 120 440 Z" fill="url(#limeBack)"/>
  </svg>
  <div class="services">
    <h2 class="services__heading">Your One-Stop Hardscape Solution For:</h2>
    <p class="services__sector">Retirement Village &amp; Community Development Construction</p>
    <ul class="services__list">
      <li class="services__item"><svg class="services__bullet" viewBox="0 0 30 14"><path d="M2 12 C10 4 20 2 28 4 C20 6 12 9 2 12 Z" fill="var(--white)"/></svg>Synthetic Sports Fields</li>
      <li class="services__item"><svg class="services__bullet" viewBox="0 0 30 14"><path d="M2 12 C10 4 20 2 28 4 C20 6 12 9 2 12 Z" fill="var(--white)"/></svg>Tennis Courts</li>
      <li class="services__item"><svg class="services__bullet" viewBox="0 0 30 14"><path d="M2 12 C10 4 20 2 28 4 C20 6 12 9 2 12 Z" fill="var(--white)"/></svg>Paving</li>
      <li class="services__item"><svg class="services__bullet" viewBox="0 0 30 14"><path d="M2 12 C10 4 20 2 28 4 C20 6 12 9 2 12 Z" fill="var(--white)"/></svg>Bowling Greens</li>
      <li class="services__item"><svg class="services__bullet" viewBox="0 0 30 14"><path d="M2 12 C10 4 20 2 28 4 C20 6 12 9 2 12 Z" fill="var(--white)"/></svg>Concreting</li>
      <li class="services__item"><svg class="services__bullet" viewBox="0 0 30 14"><path d="M2 12 C10 4 20 2 28 4 C20 6 12 9 2 12 Z" fill="var(--white)"/></svg>Landscape</li>
    </ul>
  </div>
</section>

</body>
</html>
```